Vegan bakery needs business card

We need a business card design for my vegan bakery in Philadelphia Pa. We create amazing whole food plant based cuisine that is egg and dairy free. We use fruits, vegetables, healing herbs, nuts, natural sugars (date, turbinado, agave) and non bleached flours in our creations. Due to demand and interest in the Philadelphia area we created a late night vegan dessert delivery service named Tallowbrook Vegan. We are the only business providing delicious vegan desserts delivered to your door at 1am!! We would like to see designs that use the color scheme in the logo. The final design should communicate the benefits of our products: dairy/egg free, plant based, healing herbs, amazing food.

```html
<!DOCTYPE html>
<html lang="en">
<head>
<meta charset="utf-8">
<title>Tallowbrook Vegan – Business Card</title>
<link rel="stylesheet" href="https://fonts.googleapis.com/css2?family=Ubuntu:wght@400;500&family=Arimo:wght@400&display=swap">
<style>
  :root {
    --stage: #e8e8e9;
    --card: #ffffff;
    --coral: #ef7c66;
    --coral-deep: #f06a3c;
    --leaf: #5cb547;
    --ink: #4d4d4f;
    --fruit-orange: #f47b3d;
    --fruit-peach: #f5a184;
    --fruit-berry: #a3192e;
    --fruit-lemon: #f4d21c;
  }
  * { margin: 0; padding: 0; box-sizing: border-box; }
  html, body { width: 1200px; height: 675px; overflow: hidden; }
  body {
    background: var(--stage);
    display: flex;
    align-items: center;
    justify-content: center;
    gap: 48px;
    font-family: "Ubuntu", sans-serif;
  }
  .card {
    position: relative;
    width: 528px;
    height: 302px;
    background: var(--card);
    box-shadow: 0 6px 18px rgba(0,0,0,0.12);
    overflow: hidden;
  }

  /* Front */
  .card-front .brand {
    position: absolute;
    top: 46px; left: 0; right: 0;
    text-align: center;
  }
  .brand-name {
    font-family: "Ubuntu", sans-serif;
    font-weight: 500;
    color: var(--coral);
    font-size: 34px;
    letter-spacing: 0.5px;
  }
  .brand-dot {
    display: inline-block;
    width: 14px; height: 14px;
    border-radius: 50%;
    background: var(--coral);
    margin-right: 10px;
    vertical-align: 4px;
  }
  .tagline {
    color: var(--leaf);
    font-weight: 500;
    font-size: 20px;
    line-height: 1.05;
    margin-top: 16px;
  }
  .benefit-band {
    position: absolute;
    left: 0; right: 0;
    top: 204px;
    height: 34px;
    background: var(--coral);
    color: #fff;
    font-size: 15.5px;
    font-weight: 500;
    display: flex;
    align-items: center;
    justify-content: center;
    letter-spacing: 0.2px;
  }

  /* Back */
  .card-back .artwork {
    position: absolute;
    left: 0; top: 0; bottom: 0;
    width: 290px;
    background:
      linear-gradient(170deg, var(--leaf) 0%, var(--leaf) 12%, transparent 12.5%),
      linear-gradient(180deg, var(--coral-deep) 0%, var(--fruit-orange) 45%, var(--fruit-peach) 70%, var(--fruit-berry) 88%, var(--fruit-lemon) 100%);
  }
  .contact {
    position: absolute;
    right: 22px; top: 20px;
    width: 230px;
    text-align: right;
    font-family: "Arimo", sans-serif;
    color: var(--ink);
  }
  .contact .brand-name { font-size: 19px; }
  .contact .brand-dot { width: 9px; height: 9px; margin-right: 6px; vertical-align: 2px; }
  .contact .tagline {
    font-family: "Ubuntu", sans-serif;
    font-size: 11px;
    margin-top: 6px;
    margin-bottom: 16px;
  }
  .person { font-size: 13.5px; margin-bottom: 14px; }
  .address { font-size: 13.5px; line-height: 1.2; margin-bottom: 12px; }
  .lines { list-style: none; font-size: 13.5px; line-height: 1.35; }
  .lines li { display: flex; justify-content: flex-end; align-items: center; gap: 6px; }
  .icon { width: 14px; height: 14px; flex: none; }
  .icon-blank { width: 14px; }
</style>
</head>
<body>

  <section class="card card-front" aria-label="Card front">
    <div class="brand">
      <div class="brand-name"><span class="brand-dot"></span>Tallowbrook Vegan</div>
      <p class="tagline">100% vegan<br>100% delicious</p>
    </div>
    <div class="benefit-band">Dairy/egg free, Plant based, Healing Herbs, Amazing Food</div>
  </section>

  <section class="card card-back" aria-label="Card back">
    <div class="artwork" role="img" aria-label="Large illustration of a cupcake with orange frosting and a leaf, filled with colourful fruits and vegetables"></div>
    <div class="contact">
      <div class="brand-name"><span class="brand-dot"></span>Tallowbrook Vegan</div>
      <p class="tagline">100% vegan<br>100% delicious</p>
      <p class="person">Employee Name | Title</p>
      <p class="address">Center City HQ<br>2140 Larchmere Avenue- Suite 310<br>Philadelphia, PA 19103</p>
      <ul class="lines">
        <li>(215) 555- 0147
          <svg class="icon" viewBox="0 0 14 14" aria-hidden="true"><rect width="14" height="14" rx="2" fill="var(--coral)"/><path d="M4.5 3.2c.4-.3.9-.2 1.1.2l.7 1.3c.2.4.1.8-.2 1l-.5.4c.4.9 1.1 1.6 2 2l.4-.5c.3-.3.7-.4 1-.2l1.3.7c.4.2.5.7.2 1.1l-.6.7c-.4.4-1 .5-1.5.3C6.3 9.5 4.5 7.7 3.8 5.6c-.2-.5-.1-1.1.3-1.5z" fill="#fff"/></svg>
        </li>
        <li>info@website.com
          <svg class="icon" viewBox="0 0 14 14" aria-hidden="true"><rect width="14" height="14" rx="2" fill="var(--coral)"/><rect x="2.5" y="4" width="9" height="6.5" fill="none" stroke="#fff" stroke-width="1"/><path d="M2.5 4l4.5 3.6L11.5 4" fill="none" stroke="#fff" stroke-width="1"/></svg>
        </li>
        <li>www.website.com
          <svg class="icon" viewBox="0 0 14 14" aria-hidden="true"><circle cx="7" cy="7" r="6" fill="var(--coral)"/><circle cx="7" cy="7" r="4" fill="none" stroke="#fff" stroke-width=".9"/><ellipse cx="7" cy="7" rx="1.7" ry="4" fill="none" stroke="#fff" stroke-width=".9"/><path d="M3 7h8" stroke="#fff" stroke-width=".9"/></svg>
        </li>
      </ul>
    </div>
  </section>

</body>
</html>
```